Beautiful design needed for elegant mermaid WP-website

Hi! I need a design for a website for a mermaid-website. I teach swimming (like a mermaid) and host mermaid birthday-parties for children. I don't need fancy payment options, I'd just like to showcase photo's, videos, some blogs and some information about lessons, photoshoots, et cetera.

I'm kind of in the middle on whether I would want the design to be based on pictures of me as a mermaid (I have some, but I'm going to get better ones in a few months so they'd have to be changeable without the entire design falling apart), or if I'd like it to be more like a children's book with a beautiful illustration-like design. (An illustrative design should be able to incorporate actual mermaid-photos in content).

The design should be dreamy, prefereably in green-ish and blue-ish colours, kind of like a fairytale-book. It has to be pretty romantic (I love watercolour-painting-ish designs), but not so embellished that it can't be taken seriously.

For photo's and videos, check www.coralwhisperwaves.com.
Looking forward to seeing your designs! ^^

Target Market(s)

Children's parties, swimming lessons, photoshoots, etc.

Industry/Entity Type

Painting

Number of Pages Required

3 page

Font styles to use
Serif
Decorative

Requirements
Must have
• A homepage design
• A content page design for photo's, videos and blogs
Nice to have
• Maybe a design for a contact form
Should not have
• Webshop, payment options

```html
<!DOCTYPE html>
<html lang="en">
<head>
<meta charset="utf-8">
<title>Tidewave Swimming</title>
<link href="https://fonts.googleapis.com/css2?family=Raleway:wght@400;500&family=Open+Sans:wght@400;600&display=swap" rel="stylesheet">
<style>
:root{
  --ink:#222;
  --muted:#555;
  --navy:#0e2a6b;
  --royal:#1d4f9c;
  --brand:#2f5fc4;
  --sky:#2fb3ee;
  --band:#3a86ef;
  --band-tab:#2f74dc;
  --footer:#e8e8e8;
  --white:#fff;
}
*{margin:0;padding:0;box-sizing:border-box}
html,body{width:826px;height:1200px;overflow:hidden;background:var(--white)}
body{font-family:'Open Sans',sans-serif;color:var(--ink)}
.page{position:relative;width:826px;height:1200px;overflow:hidden}

/* header */
.site-header{position:absolute;left:0;top:0;width:826px;height:60px;background:var(--white)}
.brand{position:absolute;left:116px;top:22px;font-family:'Raleway',sans-serif;font-weight:500;font-size:14px;color:var(--brand);letter-spacing:.6px;white-space:nowrap}
.main-nav a,.footer-nav a{position:absolute;font-family:'Raleway',sans-serif;font-size:9px;color:var(--ink);text-decoration:none;white-space:nowrap}
.main-nav a{top:25px}

/* hero */
.hero{position:absolute;left:0;top:60px;width:826px;height:337px;
  background:radial-gradient(ellipse 260px 150px at 620px 200px,#3fd9a6 0%,#1aa0b8 35%,transparent 75%),
             radial-gradient(ellipse 300px 90px at 160px 80px,#c9a38f 0%,#6d7fa8 45%,transparent 80%),
             linear-gradient(180deg,#1b4f9a 0%,#123f8c 40%,#0c2f78 100%)}
.hero-box{position:absolute;left:203px;top:99px;width:411px;height:113px;background:rgba(14,32,80,.72);text-align:center;color:var(--white);font-family:'Raleway',sans-serif}
.hero-box h1{font-weight:500;font-size:23px;margin-top:20px;line-height:27px}
.hero-box p{font-size:15px;line-height:18px}
.btn{position:absolute;top:72px;width:82px;height:23px;font-family:'Open Sans',sans-serif;font-size:9px;line-height:23px;color:var(--white);text-align:center}
.btn-learn{left:127px;background:var(--navy)}
.btn-join{left:213px;background:var(--sky)}
.slider-dots{position:absolute;left:756px;top:106px}

/* about */
.about h2{position:absolute;left:118px;top:438px;font-family:'Raleway',sans-serif;font-weight:400;font-size:19px;color:var(--ink)}
.about .lead{position:absolute;left:118px;top:469px;width:340px;font-size:8px;font-weight:400;line-height:11.5px;color:#444}
.about .body{position:absolute;left:118px;width:345px;font-size:6.4px;line-height:11px;color:var(--muted)}
.lessons h3{position:absolute;left:506px;top:441px;font-family:'Raleway',sans-serif;font-weight:400;font-size:15px;color:var(--royal)}
.lessons .thumb{position:absolute;left:507px;top:467px;width:69px;height:53px;background:linear-gradient(135deg,#2a4a7a,#9fa9bf 55%,#c99a86)}
.lessons .side{position:absolute;left:582px;top:467px;width:130px;font-size:6.4px;line-height:11.2px;color:var(--muted)}
.lessons .below{position:absolute;left:507px;top:526px;width:205px;font-size:6.4px;line-height:11.2px;color:var(--muted)}

/* photos */
.photos{position:absolute;left:0;top:618px;width:826px;height:263px;background:var(--band)}
.photos-tab{position:absolute;left:324px;top:0}
.photos h2{position:absolute;left:0;width:826px;top:7px;text-align:center;font-family:'Raleway',sans-serif;font-weight:400;font-size:17px;color:var(--white)}
.photo{position:absolute;width:142px;height:84px}

/* blog + videos */
.section-title{position:absolute;top:918px;font-family:'Raleway',sans-serif;font-weight:400;font-size:14px}
.blog-title{color:var(--ink);left:117px}
.video-title{color:var(--royal);left:422px}
.post h4{position:absolute;left:118px;font-family:'Raleway',sans-serif;font-weight:400;font-size:9px;color:#333}
.post p{position:absolute;left:118px;width:262px;font-size:6px;line-height:11px;color:#777}
.post .more{position:absolute;left:118px;font-size:6.4px;font-weight:600;color:var(--royal);letter-spacing:.2px}
.video{position:absolute;width:92px;height:68px}
.play{position:absolute;left:34px;top:22px}

/* footer */
.site-footer{position:absolute;left:0;top:1134px;width:826px;height:66px;background:var(--footer);box-shadow:0 -2px 4px rgba(0,0,0,.12)}
.footer-nav a{top:22px;font-size:8px}
.copyright{position:absolute;left:122px;top:38px;font-size:6.6px;color:#333}
.social{position:absolute;left:656px;top:20px;display:flex;gap:3px}
.social span{width:12px;height:12px;border-radius:2px;background:var(--royal)}
</style>
</head>
<body>
<div class="page">

  <header class="site-header">
    <div class="brand">TIDEWAVE SWIMMING</div>
    <nav class="main-nav">
      <a style="left:310px">Home</a>
      <a style="left:356px">About Nerina</a>
      <a style="left:427px">Videos</a>
      <a style="left:477px">Photography</a>
      <a style="left:550px">A Mermaid's tips</a>
      <a style="left:638px">Hire a Mermaid</a>
    </nav>
  </header>

  <section class="hero" role="img" aria-label="Underwater photograph of a mermaid swimming in a flowing green tail">
    <div class="hero-box">
      <h1>Mauris lacus vitae felis vestibulum</h1>
      <p>Sed metus augue convallis vehicula pulvinar</p>
      <div class="btn btn-learn">Learn More</div>
      <div class="btn btn-join">Join Now</div>
    </div>
    <svg class="slider-dots" width="14" height="93" viewBox="0 0 14 93">
      <rect x="0" y="0" width="14" height="93" rx="7" fill="#0b1633" opacity=".85"/>
      <circle cx="7" cy="22" r="3.4" fill="#2f74ff"/>
      <circle cx="7" cy="38" r="3.4" fill="#fff"/>
      <circle cx="7" cy="53" r="3.4" fill="#fff"/>
      <circle cx="7" cy="69" r="3.4" fill="#fff"/>
    </svg>
  </section>

  <section class="about">
    <h2>About Nerina The Siren</h2>
    <p class="lead">Mauris vel lacus vitae felis vestibulum volutpat Etiam est nunc venenatis in tristique eu imperdiet ac nisl Cum sociis natoque penatibus et magnis</p>
    <p class="body" style="top:494px">dis parturient montes nascetur ridiculus mus In iaculis facilisis massa Etiam eu urna Sed porta Suspendisse quam leo molestie sed luctus quis feugiat in pede Fusce tellus Sed metus augue convallis et vehicula ut pulvinar eu ante Integer orci tellus tristique vitae consequat nec porta vel</p>
    <p class="body" style="top:530px">Vivamus porttitor purus nisi eleifend libero a tempus libero lectus feugiat felis Morbi diam mauris viverra in gravida eu mattis in ante Morbi porta libero id ullamcorper nonummy nibh ligula pulvinar metus eget consectetuer augue nisi quis lacus Ut ac mi quis lacus mollis aliquam Curabitur iaculis temp</p>
  </section>

  <aside class="lessons">
    <h3>Lessons &amp; Photoshoot</h3>
    <div class="thumb" role="img" aria-label="Photo of a mermaid resting on a rock"></div>
    <p class="side">Morbi diam mauris viverra in gravida eu mattis in ante Morbi eget arcu Morbi porta libero id ullamcorper nonummy nibh ligula pulvinar metus eget consectetuer augue nisi quis lacus Ut ac</p>
    <p class="below">mi quis lacus mollis aliquam Curabitur iaculis tempus eros Curabitur vel mi sit amet magna malesuada ultrices Ut nisi erat fermentum vel congue id euismod</p>
  </aside>

  <section class="photos">
    <svg class="photos-tab" width="168" height="35" viewBox="0 0 168 35">
      <path d="M0 0H168L152 31Q150 35 145 35H23Q18 35 16 31Z" fill="var(--band-tab)"/>
    </svg>
    <h2>Our Photos</h2>
    <div class="photo" style="left:117px;top:54px;background:radial-gradient(circle at 55% 85%,#3be07a,#0d4a2a 40%,#062a1c)" role="img" aria-label="Mermaid glowing green in dark water"></div>
    <div class="photo" style="left:267px;top:54px;background:linear-gradient(135deg,#9fe0a0,#3fb48a 50%,#6fd0c0)" role="img" aria-label="Mermaid lying in bright green water"></div>
    <div class="photo" style="left:418px;top:54px;background:linear-gradient(180deg,#e39a9a,#4a8fcf 40%,#2a5ea8)" role="img" aria-label="Mermaid swimming under a pink sky"></div>
    <div class="photo" style="left:568px;top:54px;background:linear-gradient(135deg,#0d3b20,#2f7a3a 55%,#0a2a16)" role="img" aria-label="Mermaid holding a rope underwater"></div>
    <div class="photo" style="left:117px;top:144px;background:linear-gradient(135deg,#c9a07a,#a8362a 45%,#d6b088)" role="img" aria-label="Fish among red coral"></div>
    <div class="photo" style="left:267px;top:144px;background:radial-gradient(circle at 60% 40%,#2fc0a0,#0a2f4a 55%,#06182c)" role="img" aria-label="Mermaid diving in deep water"></div>
    <div class="photo" style="left:418px;top:144px;background:linear-gradient(135deg,#7fe0ff,#1aa6e6 50%,#0a3a6a)" role="img" aria-label="Silhouette of a mermaid in light blue water"></div>
    <div class="photo" style="left:568px;top:144px;background:radial-gradient(circle at 50% 50%,#0a1a5a,#1236c8 60%,#1e4ee0)" role="img" aria-label="Mermaid silhouette in deep blue"></div>
  </section>

  <h2 class="section-title blog-title">Latest Blog Post</h2>
  <article class="post">
    <h4 style="top:942px">Vivamus porttitor purus nisi eleifend libero</h4>
    <p style="top:955px">Cum sociis natoque penatibus et magnis dis parturient montes nascetur ridiculus mus In iaculis facilisis massa Etiam eu urna Sed porta Suspendisse quam leo molestie sed luctus quis feugiat in pede Fusce</p>
    <span class="more" style="top:991px">READ MORE</span>
  </article>
  <article class="post">
    <h4 style="top:1016px">Class aptent taciti sociosqu ad litor</h4>
    <p style="top:1029px">Cum sociis natoque penatibus et magnis dis parturient montes nascetur ridiculus mus In iaculis facilisis massa Etiam eu urna Sed porta Suspendisse quam leo molestie sed luctus quis feugiat in pede Fusce</p>
    <span class="more" style="top:1065px">READ MORE</span>
  </article>

  <h2 class="section-title video-title">Watch Our Videos</h2>
  <div class="video" style="left:422px;top:946px;background:linear-gradient(135deg,#2a5a4a,#163a34)" role="img" aria-label="Video still of an underwater forest">
    <svg class="play" width="24" height="24"><circle cx="12" cy="12" r="11" fill="#fff"/><path d="M9 7L17 12L9 17Z" fill="#111"/></svg></div>
  <div class="video" style="left:519px;top:946px;background:linear-gradient(135deg,#1a2a3a,#b0704a 55%,#2a3a4a)" role="img" aria-label="Video still of a mermaid portrait">
    <svg class="play" width="24" height="24"><circle cx="12" cy="12" r="11" fill="#fff"/><path d="M9 7L17 12L9 17Z" fill="#111"/></svg></div>
  <div class="video" style="left:617px;top:946px;background:linear-gradient(135deg,#5ab8d8,#1f7fb0)" role="img" aria-label="Video still of a mermaid swimming">
    <svg class="play" width="24" height="24"><circle cx="12" cy="12" r="11" fill="#fff"/><path d="M9 7L17 12L9 17Z" fill="#111"/></svg></div>
  <div class="video" style="left:422px;top:1020px;background:linear-gradient(135deg,#1a5a7a,#3ab0d0 50%,#0e3a5a)" role="img" aria-label="Video still of a mermaid tail in light rays">
    <svg class="play" width="24" height="24"><circle cx="12" cy="12" r="11" fill="#fff"/><path d="M9 7L17 12L9 17Z" fill="#111"/></svg></div>
  <div class="video" style="left:519px;top:1020px;background:linear-gradient(180deg,#6a7a6a,#a89070 60%,#4a4a3a)" role="img" aria-label="Video still of a mermaid on a rock">
    <svg class="play" width="24" height="24"><circle cx="12" cy="12" r="11" fill="#fff"/><path d="M9 7L17 12L9 17Z" fill="#111"/></svg></div>
  <div class="video" style="left:617px;top:1020px;background:linear-gradient(135deg,#8acbe0,#2a7ab0)" role="img" aria-label="Video still of a mermaid underwater">
    <svg class="play" width="24" height="24"><circle cx="12" cy="12" r="11" fill="#fff"/><path d="M9 7L17 12L9 17Z" fill="#111"/></svg></div>

  <footer class="site-footer">
    <nav class="footer-nav">
      <a style="left:122px">Home</a>
      <a style="left:162px">About Nerina</a>
      <a style="left:225px">Videos</a>
      <a style="left:268px">Photography</a>
      <a style="left:333px">A Mermaid's tips</a>
      <a style="left:411px">Hire a Mermaid</a>
    </nav>
    <p class="copyright">© 2015 Company Name&nbsp; All right reserved&nbsp; Term of Use</p>
    <div class="social" aria-label="Social links"><span></span><span></span><span></span></div>
  </footer>

</div>
</body>
</html>
```